Website Design Project for Beauty & Wellness Professionals

As background information, I have a website that is focused on Beauty & Wellness Professionals:
- Job Search (www.trilhavelora.com)
- Business Classifieds (negocios.trilhavelora.com)
- Freelancer Classifieds (freelancer.trilhavelora.com)
- Course Reviews (cursos.trilhavelora.com)

All those websites use standard templates.

I need a DESIGN for the HOME PAGE (no coding) of the Website Platform that consolidates the four platforms under the same design.

Website designs that we like:
- nestorly.com
- workpane.com

Target Market(s)

Brazilian Professionals from Beauty & Wellness sector

Industry/Entity Type

Business

Requirements
Must have
• Website designs that we like:
- nestorly.com
- workpane.com

```html
<!DOCTYPE html>
<html lang="en">
<head>
<meta charset="utf-8">
<title>Trilha Velora – Home</title>
<link href="https://fonts.googleapis.com/css2?family=Fira+Sans+Condensed:wght@600&family=Open+Sans:ital,wght@0,300;0,400;0,600;0,700;1,400;1,700&family=Raleway:wght@300;400&display=swap" rel="stylesheet">
<style>
:root{
  --teal:#2b93bf;
  --teal-dark:#1f7ea8;
  --teal-light:#4cb0d6;
  --orange:#e06a34;
  --orange-text:#e8702d;
  --ink:#222;
  --body:#444;
  --link:#1a75b0;
  --panel:#f3f3f3;
  --footer:#2e2e2e;
  --footer-bar:#1d1d1d;
  --star:#2f8a2f;
}
*{box-sizing:border-box;margin:0;padding:0}
html,body{width:845px;height:1200px;overflow:hidden;background:#fff}
body{position:relative;font-family:"Open Sans",Arial,sans-serif;color:var(--body)}
.abs{position:absolute}

/* header */
.brand{left:72px;top:26px;display:flex;align-items:center;gap:8px}
.brand-dot{width:22px;height:22px;border-radius:50%;background:var(--teal)}
.brand-name{font-size:22px;color:var(--teal)}
.contact{left:584px;top:32px;display:flex;gap:10px;align-items:center}
.phone-ico{width:26px;height:26px;border-radius:50%;background:#e4e4e4;display:flex;align-items:center;justify-content:center}
.phone-num{font-size:17px;font-weight:700;color:var(--ink);line-height:20px}
.email{font-size:12px;color:var(--link);text-decoration:underline;display:block;text-align:right}

/* nav */
.nav{left:0;top:92px;width:845px;height:32px;background:linear-gradient(#45a9d1,var(--teal-dark));display:flex;align-items:center;padding-left:74px}
.nav a{color:#fff;font-size:12px;text-decoration:none;padding:0 20px;border-right:1px solid rgba(255,255,255,.25);line-height:18px}
.nav a:last-child{border-right:none}

/* hero */
.hero{left:0;top:124px;width:845px;height:242px;
  background:
    radial-gradient(ellipse 260px 110px at 350px 110px,rgba(240,236,220,.55),transparent 70%),
    radial-gradient(ellipse 300px 90px at 720px 80px,rgba(150,140,70,.7),transparent 70%),
    radial-gradient(ellipse 260px 80px at 60px 150px,rgba(120,60,30,.65),transparent 70%),
    linear-gradient(180deg,#8d8a5e 0%,#a09a6a 22%,#6d6a3f 45%,#4a3f28 60%,#6a5a3a 72%,#3a2d1c 86%,#20180e 100%)}
.hero-title{left:0;top:210px;width:845px;text-align:center;font-family:"Fira Sans Condensed",sans-serif;font-weight:600;font-size:32px;color:#fff;letter-spacing:.5px;text-shadow:0 2px 3px rgba(0,0,0,.6)}
.search{left:96px;top:262px;width:630px;height:39px;background:rgba(0,0,0,.6);border-radius:3px}
.search .field{position:absolute;top:4px;height:31px;background:#fff;border-radius:3px;font-size:12px;color:#888;padding:8px 9px}
.search .q{left:4px;width:326px}
.search .cat{left:341px;width:199px}
.search .caret{position:absolute;right:0;top:4px;width:32px;height:23px;border-left:1px solid #ccc}
.search .go{position:absolute;left:545px;top:4px;width:81px;height:31px;background:var(--orange);border-radius:3px;color:#fff;font-size:17px;text-align:center;line-height:31px}

/* about section */
.panel{left:0;top:366px;width:845px;height:434px;background:var(--panel)}
.h-sec{font-family:"Raleway",sans-serif;font-weight:300;color:var(--ink)}
.what-h{left:77px;top:386px;font-size:22px;letter-spacing:1px}
.what-rule{left:76px;top:418px;width:396px;border-top:1px dotted #bbb}
.what-text{left:76px;top:426px;width:438px;font-family:Arial,Helvetica,sans-serif;font-size:8.4px;line-height:15.6px;text-align:justify;color:#333}
.what-text p{margin-bottom:6px}
.more{left:455px;top:533px;width:55px;height:17px;background:var(--orange);border-radius:9px;color:#fff;font-size:9px;font-weight:600;line-height:17px;padding-left:9px}
.more span{position:absolute;right:-2px;top:-1px;width:19px;height:19px;border-radius:50%;background:#fff;border:1px solid #ccc;color:#555;font-size:13px;line-height:16px;text-align:center}
.vrule{left:544px;top:398px;height:142px;border-left:1px dotted #bbb}
.testi{left:558px;top:388px;width:210px;height:174px;background:#fff;border-radius:12px;box-shadow:0 1px 3px rgba(0,0,0,.08)}
.testi-h{position:absolute;left:14px;top:12px;display:flex;gap:6px;align-items:center;font-size:16px;color:var(--orange-text)}
.testi-q{position:absolute;left:18px;top:52px;width:180px;font-size:7.5px;line-height:14px;color:#444;text-align:justify}
.testi-by{position:absolute;right:12px;top:150px;font-size:8px;font-weight:700;font-style:italic;color:var(--orange-text);text-decoration:underline}
.hrule{left:73px;top:582px;width:700px;border-top:1px solid #d8d8d8}

/* tabs */
.tabs{left:80px;top:606px;width:466px;height:182px}
.tab-row{display:flex;height:30px}
.tab{font-family:"Raleway",sans-serif;font-size:16px;color:#333;padding:6px 18px 0}
.tab.on{background:#fff;color:var(--teal);border:1px solid #e2e2e2;border-bottom:none;border-radius:4px 4px 0 0;padding:6px 26px 0}
.tab-body{background:#fff;border:1px solid #e2e2e2;height:152px;padding:8px 12px}
.rev{display:flex;gap:8px;height:68px;position:relative;margin-bottom:10px}
.rev-logo{width:56px;height:56px;flex:none;background:#111;border:1px solid #999;display:flex;align-items:center;justify-content:center}
.rev-logo i{width:22px;height:22px;background:#555;display:block}
.rev-logo.b{background:#24307a}
.rev-name{width:76px;flex:none;font-family:Arial,Helvetica,sans-serif}
.rev-name b{display:block;font-size:10px;color:var(--teal-dark);font-weight:700;white-space:nowrap}
.stars{color:var(--star);font-size:12px;letter-spacing:-1px;line-height:15px}
.stars s{color:#ccc;text-decoration:none}
.rev-name small{font-size:8px;color:#777}
.rev-txt{width:294px;font-family:Arial,Helvetica,sans-serif;font-size:7.6px;line-height:11.5px;color:#444}
.rev-txt strong{display:block;font-size:8.6px;line-height:12.5px;color:var(--teal-dark);font-weight:700;margin-bottom:3px;letter-spacing:.2px}
.readmore{position:absolute;right:10px;bottom:-4px;font-size:7.5px;font-style:italic;color:#333}

/* ad */
.ad{left:562px;top:618px;width:211px;height:167px;background:linear-gradient(#bcbec1,#d6d7d9)}
.ad-brand{position:absolute;left:9px;top:9px;font-size:13px;font-weight:700;color:#fff}
.ad-line{position:absolute;left:63px;top:8px;font-size:13px;color:#fff;line-height:17px;letter-spacing:.5px}
.ad-mark{position:absolute;right:3px;top:2px;width:9px;height:9px;background:var(--teal)}
.ad-art{position:absolute;left:10px;top:54px;width:190px;height:110px;border-radius:6px;
  background:
    radial-gradient(ellipse 70px 30px at 70px 32px,rgba(214,60,55,.85),transparent 75%),
    radial-gradient(ellipse 26px 48px at 170px 62px,rgba(226,70,50,.9),transparent 80%),
    linear-gradient(#3c3c3c,#f2f2f2 18%,#e8e8e8 70%,#555 100%)}

/* featured */
.feat-h{left:77px;top:818px;font-size:22px;letter-spacing:.5px}
.card{top:856px;width:158px;height:136px;background:#fff;border:1px solid #e4e4e4;border-radius:4px;padding:5px}
.card div{width:100%;height:124px}

/* footer */
.footer{left:0;top:1022px;width:845px;height:158px;background:var(--footer);color:#ddd}
.f-col{position:absolute;top:16px}
.f-h{font-family:"Raleway",sans-serif;font-weight:300;font-size:16px;color:#eee;padding-bottom:10px;border-bottom:1px solid #444}
.f-list{list-style:none;margin-top:16px;font-family:Arial,sans-serif;font-size:8.5px;line-height:16px}
.f-list li:before{content:"";display:inline-block;width:3px;height:3px;background:var(--teal-light);border-radius:50%;margin:0 7px 2px 0}
.tweet{margin-top:16px;position:relative;font-family:Arial,sans-serif;font-size:8.5px;line-height:11.5px}
.tweet-av{position:absolute;left:0;top:0;width:20px;height:20px;background:#c89a4a;border-radius:2px}
.f-p{margin-top:16px;font-family:Arial,sans-serif;font-size:8.5px;line-height:14px}
.mail{margin-top:10px;width:162px;height:23px;background:#e2e2e2;font-size:7.5px;color:#999;padding:7px 8px;display:flex;gap:7px}
.soc{display:flex;gap:8px;margin-top:14px}
.soc i{width:14px;height:14px;border-radius:50%;background:#e6e6e6;display:block}
.cards{display:flex;gap:8px;margin-top:12px}
.cards i{width:15px;height:9px;background:#cfcfcf;display:block;border-radius:1px}
.f-bar{left:0;top:1180px;width:845px;height:20px;background:var(--footer-bar);color:#eee;font-family:Arial,sans-serif;font-size:8.5px;text-align:center;line-height:20px}
</style>
</head>
<body>

<header>
  <div class="abs brand"><span class="brand-dot"></span><span class="brand-name">Trilha Velora</span></div>
  <div class="abs contact">
    <span class="phone-ico"><svg width="13" height="13" viewBox="0 0 24 24"><path fill="#777" d="M6.6 10.8a15 15 0 0 0 6.6 6.6l2.2-2.2c.3-.3.7-.4 1-.2 1.1.4 2.3.6 3.6.6.6 0 1 .4 1 1V20c0 .6-.4 1-1 1A17 17 0 0 1 3 4c0-.6.4-1 1-1h3.5c.6 0 1 .4 1 1 0 1.3.2 2.5.6 3.6.1.3 0 .7-.2 1z"/></svg></span>
    <div><div class="phone-num">(415)-820-(3391)</div><a class="email">info@trilhavelora.com</a></div>
  </div>
</header>

<nav class="abs nav">
  <a>Home</a><a>Categories of Business</a><a>For Professionals</a><a>For Business</a><a>About Us</a><a>Contact Us</a>
</nav>

<section class="abs hero" role="img" aria-label="Photo of a fishing boat moored on a calm harbour at dusk with hills behind"></section>
<h1 class="abs hero-title">Welcome to the presentation of Trilha Velora</h1>
<div class="abs search">
  <div class="field q">what are you looking for?</div>
  <div class="field cat">All Categories
    <span class="caret"><svg width="32" height="23" viewBox="0 0 32 23"><path d="M11 9h10l-5 6z" fill="#444"/></svg></span>
  </div>
  <div class="go">Search</div>
</div>

<section class="abs panel"></section>
<h2 class="abs h-sec what-h">What We Do</h2>
<div class="abs what-rule"></div>
<div class="abs what-text">
  <p><b><i>Lorem Ipsum is simply dummy text of the printing and typesetting industry. Lorem Ipsum has been the industry's standard dummy text ever since the 1500s,</i></b> when an unknown printer took a galley of type and scrambled it to make a type specimen book. It has survived not only five centuries, but also the leap into electronic typesetting, remaining essentially unchanged.</p>
  <p>It was popularised in the 1960s with the release of Lettrane sheets containing Lorem Ipsum passages, and more recently with desktop publishing software like Pagecraft including versions of Lorem Ipsum.</p>
</div>
<div class="abs more">More<span>+</span></div>
<div class="abs vrule"></div>

<aside class="abs testi">
  <div class="testi-h"><svg width="30" height="22" viewBox="0 0 30 22"><ellipse cx="11" cy="9" rx="10" ry="7" fill="#e8702d"/><path d="M5 14l-2 6 7-4z" fill="#e8702d"/><ellipse cx="19" cy="12" rx="10" ry="7" fill="#f08a4b"/></svg>Testimonials</div>
  <p class="testi-q">&ldquo; <b><i>Lorem Ipsum is simply dummy text of the printing and typesetting industry.</i></b> Lorem Ipsum has been the industry's standard dummy text ever since the 1500s, when an unknown printer took a galley of type and scrambled it to make a type. scrambled it to make a type. &rdquo;</p>
  <div class="testi-by">says : Marla Quent</div>
</aside>
<div class="abs hrule"></div>

<section class="abs tabs">
  <div class="tab-row"><span class="tab on">Recents</span><span class="tab">Most Viewed</span><span class="tab">Random</span></div>
  <div class="tab-body">
    <div class="rev">
      <div class="rev-logo"><i></i></div>
      <div class="rev-name"><b>Telvanta</b><div class="stars">★★★<s>★★</s></div><small>1,429 reviews</small></div>
      <div class="rev-txt"><strong>&ldquo; simply dummy text of the printing and typesetting industry. Lorem Ipsum has been the industry's</strong>simply dummy text of the printing and typesetting industry. Lorem Ipsum has been the industry's</div>
      <span class="readmore">read more...</span>
    </div>
    <div class="rev">
      <div class="rev-logo b"><i></i></div>
      <div class="rev-name"><b>Norbrook Bank</b><div class="stars">★★★<s>★★</s></div><small>820 reviews</small></div>
      <div class="rev-txt"><strong>&ldquo; simply dummy text of the printing and typesetting industry. Lorem Ipsum has been the industry's &rdquo;</strong>simply dummy text of the printing and typesetting industry. Lorem Ipsum has been the industry's</div>
      <span class="readmore">read more...</span>
    </div>
  </div>
</section>

<aside class="abs ad">
  <span class="ad-brand">Tabulo</span>
  <span class="ad-line">Easy Pricing Tables<br>for Your Website</span>
  <span class="ad-mark"></span>
  <div class="ad-art" role="img" aria-label="Laptop and phone showing red and white pricing table layouts"></div>
</aside>

<h2 class="abs h-sec feat-h">Featured Listing</h2>
<div class="abs card" style="left:74px"><div role="img" aria-label="City skyline across a river with a statue on the bank" style="background:radial-gradient(ellipse 40px 12px at 60px 20px,#fff,transparent 80%),radial-gradient(ellipse 50px 10px at 110px 40px,#f4f6fa,transparent 80%),linear-gradient(#3f7fd0 0%,#87b3e0 40%,#9ea99a 55%,#6f8a7a 68%,#a6a396 82%,#c9c0ae 100%)"></div></div>
<div class="abs card" style="left:253px"><div role="img" aria-label="Roller coaster loops against a deep blue sky" style="background:radial-gradient(ellipse 40px 60px at 70px 60px,rgba(230,230,235,.85),transparent 75%),radial-gradient(ellipse 50px 16px at 110px 90px,rgba(200,70,60,.7),transparent 80%),linear-gradient(#16489e,#2f6bc0 55%,#6a8fa8 80%,#7d8a5a 100%)"></div></div>
<div class="abs card" style="left:432px"><div role="img" aria-label="Clock tower and parliament buildings with a flag and red buses" style="background:radial-gradient(ellipse 36px 22px at 30px 18px,rgba(200,40,50,.8),transparent 80%),radial-gradient(ellipse 14px 70px at 100px 70px,rgba(190,160,100,.95),transparent 85%),radial-gradient(ellipse 30px 10px at 25px 110px,rgba(210,30,30,.85),transparent 80%),linear-gradient(#2d6fc6,#6c9bd1 45%,#9b8766 70%,#6b6a66 100%)"></div></div>
<div class="abs card" style="left:611px"><div role="img" aria-label="Ornate temple spire with a golden figure in front" style="background:radial-gradient(ellipse 60px 80px at 75px 75px,rgba(180,150,110,.95),transparent 80%),radial-gradient(ellipse 12px 30px at 72px 105px,rgba(220,170,40,.95),transparent 85%),linear-gradient(#3f78c0,#7a9ac0 30%,#8b7550 65%,#5c4a30 100%)"></div></div>

<footer class="abs footer">
  <div class="f-col" style="left:82px;width:96px">
    <div class="f-h">Navigation</div>
    <ul class="f-list"><li>About Us</li><li>Best sellers</li><li>News</li><li>Collections</li></ul>
  </div>
  <div class="f-col" style="left:202px;width:234px">
    <div class="f-h">Latest tweets</div>
    <div class="tweet">
      <span class="tweet-av"></span>
      <div style="margin-left:25px"><b style="color:#eee">Brightloom</b><span style="float:right;font-size:7px">11 Jul</span><br><span style="color:#aaa">@TheBrightloom</span></div>
      <p style="margin-top:3px">We are in the final stages of building our latest product - Solvane for Pressly. It's going to use the amazing Shopkit plugin.</p>
    </div>
  </div>
  <div class="f-col" style="left:458px;width:162px">
    <div class="f-h">Newsletter</div>
    <p class="f-p">Vestibulum at lacus id turpis malesuada varius. Donec ultricies mauris vel nisi porta dictum.</p>
    <div class="mail"><svg width="9" height="7" viewBox="0 0 9 7"><rect width="9" height="7" fill="#666"/><path d="M0 0l4.5 4L9 0" stroke="#ddd" fill="none"/></svg>e-mail address</div>
  </div>
  <div class="f-col" style="left:645px;width:128px">
    <div class="f-h">About us</div>
    <p class="f-p">Solvane is a modern responsive HTML5 theme</p>
    <div class="soc"><i></i><i></i><i></i><i></i><i></i></div>
    <div class="cards"><i></i><i></i><i></i><i></i><i></i><i></i></div>
  </div>
</footer>
<div class="abs f-bar">Except where noted, copyright © 2010-2012 Trilha Velora</div>

</body>
</html>
```